Orva Business Card

we need a business card for flooring business called Orva Flooring, the design should be black and white. we have 2 locations

Wenbury Showroom
527 Kellerman Road,
Wenbury VIC 3128

Harlow Park Showroom
462 Bramwell Hwy,
Harlow Park VIC 3187

email : sales@orvaflooring.com.au
(03) 9471 2830

Please inform we sell , Laminate, Hybrid, Timber, carpet and commercial flooring

```html
<!DOCTYPE html>
<html lang="en">
<head>
<meta charset="UTF-8">
<title>Orva Flooring Business Card</title>
<link href="https://fonts.googleapis.com/css2?family=Poppins:wght@400;600&display=swap" rel="stylesheet">
<style>
  :root {
    --page: #e9e6e1;
    --card: #212325;
    --ink: #ffffff;
    --ink-soft: #e4e4e4;
  }
  * { margin: 0; padding: 0; box-sizing: border-box; }
  html, body {
    width: 1189px; height: 1200px; overflow: hidden;
    background: var(--page);
    font-family: "Poppins", sans-serif;
    color: var(--ink);
  }
  .cards {
    position: absolute; left: 142px; top: 202px;
    display: flex; gap: 19px;
  }
  .card {
    position: relative; width: 436px; height: 763px;
    background: var(--card);
    box-shadow: 0 4px 14px rgba(0,0,0,0.25);
  }
  .wordmark {
    position: absolute;
    font-weight: 400; line-height: 1; text-align: center;
    color: var(--ink);
  }
  .wordmark .name { display: block; letter-spacing: 6px; }
  .wordmark .sub { display: block; letter-spacing: 0.5px; }
  .card-front .wordmark { left: 58px; top: 566px; width: 222px; }
  .card-front .wordmark .name { font-size: 76px; margin-bottom: 12px; }
  .card-front .wordmark .sub { font-size: 42px; }
  .card-back .wordmark { left: 86px; top: 150px; width: 264px; }
  .card-back .wordmark .name { font-size: 88px; margin-bottom: 12px; }
  .card-back .wordmark .sub { font-size: 48px; }
  .services {
    position: absolute; left: 362px; bottom: 51px;
    writing-mode: vertical-rl; transform: rotate(180deg);
    font-size: 18px; letter-spacing: 0.7px; white-space: nowrap;
    color: var(--ink-soft);
  }
  .contacts { position: absolute; left: 48px; top: 458px; }
  .contact {
    display: flex; align-items: flex-start; margin-bottom: 26px;
  }
  .contact .icon { width: 16px; margin-top: 4px; margin-right: 6px; flex: none; }
  .contact .lines {
    font-size: 18px; line-height: 24px; color: var(--ink-soft);
  }
  .contact .lines > div { padding-left: 7px; }
  .contact .heading {
    font-weight: 600; color: var(--ink);
    border-left: 1px solid var(--ink);
  }
  .contact.digital .lines { border-left: 1px solid var(--ink); }
  .icon-stack { display: flex; flex-direction: column; gap: 10px; margin-top: 6px; margin-right: 6px; width: 16px; flex: none; }
</style>
</head>
<body>
  <div class="cards">
    <section class="card card-front">
      <div class="wordmark"><span class="name">ORVA</span><span class="sub">FLOORING</span></div>
      <p class="services">SELL , LAMINATE, HYBRID, TIMBER, CARPET AND COMMERCIAL FLOORING</p>
    </section>

    <section class="card card-back">
      <div class="wordmark"><span class="name">ORVA</span><span class="sub">FLOORING</span></div>

      <div class="contacts">
        <div class="contact">
          <svg class="icon" viewBox="0 0 16 20" width="14" height="18" aria-hidden="true">
            <path d="M8 1.5a5.5 5.5 0 0 0-5.5 5.5c0 4 5.5 11 5.5 11s5.5-7 5.5-11A5.5 5.5 0 0 0 8 1.5z" fill="none" stroke="#fff" stroke-width="1.5"/>
            <circle cx="8" cy="7" r="2" fill="none" stroke="#fff" stroke-width="1.5"/>
          </svg>
          <div class="lines">
            <div class="heading">HARLOW PARK SHOWROOM</div>
            <div>462 Bramwell Hwy,</div>
            <div>Harlow Park VIC 3187</div>
          </div>
        </div>

        <div class="contact">
          <svg class="icon" viewBox="0 0 16 20" width="14" height="18" aria-hidden="true">
            <path d="M8 1.5a5.5 5.5 0 0 0-5.5 5.5c0 4 5.5 11 5.5 11s5.5-7 5.5-11A5.5 5.5 0 0 0 8 1.5z" fill="none" stroke="#fff" stroke-width="1.5"/>
            <circle cx="8" cy="7" r="2" fill="none" stroke="#fff" stroke-width="1.5"/>
          </svg>
          <div class="lines">
            <div class="heading">WENBURY SHOWROOM</div>
            <div>527 Kellerman Road,</div>
            <div>Wenbury VIC 3128</div>
          </div>
        </div>

        <div class="contact digital">
          <div class="icon-stack">
            <svg viewBox="0 0 16 12" width="14" height="11" aria-hidden="true">
              <rect x="0.5" y="0.5" width="15" height="11" fill="#fff"/>
              <path d="M0.5 0.5 L8 7 L15.5 0.5 M0.5 11.5 L6 5.5 M15.5 11.5 L10 5.5" stroke="#212325" stroke-width="1.2" fill="none"/>
            </svg>
            <svg viewBox="0 0 16 16" width="14" height="14" aria-hidden="true">
              <path d="M4 1.5 L6.5 4.5 L5 6.5 C6 9 7.5 10.5 10 11.5 L12 10 L14.5 12.5 L12.5 14.5 C7 13.5 2.5 9 1.5 3.5 Z" fill="#fff"/>
            </svg>
          </div>
          <div class="lines">
            <div>sales@orvaflooring.com.au</div>
            <div>(03) 9471 2830</div>
          </div>
        </div>
      </div>
    </section>
  </div>
</body>
</html>
```